Webdesign für einen gemeinnützigen Verein
Zielgruppe
Merovalien e. V. ist ein gemeinnütziger Verein der sich auf die Fahne geschrieben hat sich für Inklusive und Vielfalt einzusetzen. Wir unterstützen Menschen mit Behinderung beim selbstbestimmten Leben und helfen auch bei Anträgen etc. Des weiteren helfen wir Firmen, Vereinen und stonstigen Organisationen Ihre Inhalte und Auftritte barrierefrei zu gestallten. Wir Testen Apps und Websites und geben hier Feedback.
Aufgabenstellung
Wir möchten ein WordPress Theme das responsiv und persistent ist. Wir möchten die Inhalte später mit WordPress Einpflege und die Seite managen.
Unser Corporate Design steht bereits und beinhaltet die Pride Farben und sollte somit in einem hellen und dunklen Design umgesetzt werden. Wir möchten hier 2 Varianten vom Homepage Design (Darkmode)
Poppins ist unsere Schriftart für Textinhalte
Google Fonds möchten wir nicht nutzen
Passende Social Media Icons

```html
<!DOCTYPE html>
<html lang="de">
<head>
<meta charset="utf-8">
<title>Merovalien e. V. – Webdesign Darkmode</title>
<link href="https://fonts.googleapis.com/css2?family=Poppins:wght@300;400;500;600&display=swap" rel="stylesheet">
<style>
:root{
  --board:#ebebeb;
  --navy:#111833;
  --purple:#4b0f63;
  --purple-2:#3a1458;
  --white:#ffffff;
  --link:#2f8fe0;
  --input:#9b9fb3;
  --rainbow:linear-gradient(90deg,#e63b2e,#f18a1f,#f5d21c,#3bb54a,#2b7de0,#7b3fc0,#b23aa8);
  --brand:'Poppins',sans-serif;
}
*{box-sizing:border-box;margin:0;padding:0}
html,body{width:1200px;height:2434px;overflow:hidden;background:var(--board);font-family:var(--brand);color:var(--white)}
.board{position:relative;width:1200px;height:2434px}
.artboard{position:absolute;top:43px;overflow:hidden}
.mobile{left:42px;width:260px;height:2306px}
.desktop{left:338px;width:820px;height:2073px}
.block{position:absolute;left:0;width:100%}
.splash{top:0;height:461px;background:linear-gradient(90deg,var(--purple) 0%,var(--navy) 100%)}
.splash .name{position:absolute;left:0;right:0;top:218px;text-align:center;font-size:20px;font-weight:500;letter-spacing:.5px}
.splash .bar{position:absolute;left:50%;top:284px;width:142px;height:3px;margin-left:-71px;border-radius:2px;background:var(--rainbow)}
.header{height:60px;background:var(--navy);display:flex;align-items:center}
.brand{display:flex;align-items:center;gap:6px;font-size:13px;font-weight:500;letter-spacing:.3px;text-transform:uppercase}
.brand .dot{width:10px;height:10px;border-radius:50%;background:var(--white)}
.mobile .brand{font-size:11px}
.mobile .header{padding:0 16px;justify-content:space-between}
.menu-btn{width:20px;height:20px;border-radius:50%;background:var(--rainbow);display:flex;flex-direction:column;justify-content:center;align-items:center;gap:2px}
.menu-btn i{display:block;width:11px;height:1.6px;background:var(--white)}
.desktop .header{padding:0 50px}
.nav{display:flex;gap:17px;margin-left:86px;font-size:10.5px}
.nav a{color:var(--white);text-decoration:none}
.nav a.active{background:var(--rainbow);border-radius:7px;padding:0 6px;color:var(--navy)}
.toggle{margin-left:auto;width:44px;height:22px;border-radius:11px;background:var(--purple-2);display:flex;align-items:center;justify-content:space-around;padding:0 4px}
.hero{height:401px}
.hero .photo{position:absolute;top:0;height:401px;background:linear-gradient(180deg,#eceae6 0%,#d9d6d1 60%,#b8b3ad 100%)}
.mobile .hero{background:var(--navy)}
.mobile .hero .photo{left:0;width:260px}
.desktop .hero{background:linear-gradient(90deg,var(--purple) 0,var(--purple) 49px,var(--navy) 49px)}
.desktop .hero .photo{left:49px;width:720px}
.cta{position:absolute;top:327px;transform:translateX(-50%);background:var(--purple);color:var(--white);font-size:8px;font-weight:600;letter-spacing:.3px;padding:6px 8px;border-radius:12px;white-space:nowrap}
.mobile .cta{left:128px}
.desktop .cta{left:409px}
.chev{position:absolute;top:358px;transform:translateX(-50%)}
.mobile .chev{left:128px}
.desktop .chev{left:409px}
.navy{background:var(--navy)}
.violet{background:linear-gradient(90deg,var(--purple) 0%,var(--navy) 100%)}
h2{font-weight:600;text-align:center;text-transform:uppercase;letter-spacing:.2px}
.mobile h2{font-size:14px;line-height:19px}
.desktop h2{font-size:21px}
.pic{position:absolute;border-radius:10px}
.pic.hands{background:linear-gradient(160deg,#c9d3e0 0%,#e7c3a6 45%,#b88a6d 75%,#dfe3ea 100%)}
.pic.group{background:linear-gradient(160deg,#8a8f9a 0%,#d8c274 40%,#3c63a6 70%,#6b5b4a 100%)}
.copy{position:absolute;text-align:justify}
.copy p + p{margin-top:1em}
.mobile .copy{left:16px;width:228px;font-size:6.4px;line-height:11.2px;letter-spacing:.1px}
.desktop .copy{font-size:10.6px;line-height:15.4px}
.copy b{font-weight:600}
.up{position:absolute;width:22px;height:22px;border-radius:50%;border:1.5px solid var(--white);display:flex;align-items:center;justify-content:center}
.footer{background:linear-gradient(180deg,var(--purple) 0%,var(--navy) 55%)}
.foot-name{font-size:17px;font-weight:500;letter-spacing:.5px;text-transform:uppercase}
.tagline{font-size:9px;line-height:10px;text-align:center}
.tagline .rule{display:flex;align-items:center;gap:4px;justify-content:center}
.tagline .rule::before,.tagline .rule::after{content:"";width:26px;height:1px;background:var(--white)}
.list{list-style:none;font-size:9.5px;font-weight:300;line-height:18px}
.list .lbl{display:inline-block;width:40px}
.email{width:142px;height:16px;border-radius:4px;background:var(--input);font-size:8.5px;color:var(--white);padding:2px 6px;font-weight:300}
.newsletter{color:var(--link)}
.copyright{position:absolute;left:0;width:100%;height:21px;background:var(--rainbow);font-size:8px;display:flex;align-items:center;justify-content:center;gap:3px}
.copyright b{font-weight:600}
.mobile .copyright{justify-content:flex-start;padding-left:47px;font-size:6.5px}
</style>
</head>
<body>
<main class="board">

  <section class="artboard mobile">
    <div class="block splash">
      <div class="name">merovalien</div>
      <div class="bar"></div>
    </div>
    <header class="block header" style="top:461px">
      <div class="brand"><span class="dot"></span>Merovalien</div>
      <div class="menu-btn"><i></i><i></i><i></i></div>
    </header>
    <div class="block hero" style="top:521px">
      <div class="photo" role="img" aria-label="Foto: Vier Frauen, eine im Rollstuhl, halten bunte Sprechblasen vor einer weißen Wand"></div>
      <div class="cta">AUSFÜHRLICHE INFOS</div>
      <svg class="chev" width="16" height="9" viewBox="0 0 16 9"><path d="M1 1l7 7 7-7" fill="none" stroke="#fff" stroke-width="1.3"/></svg>
    </div>
    <div class="block navy" style="top:922px;height:460px">
      <h2 style="margin-top:20px">Was macht uns aus?</h2>
      <div class="pic hands" style="left:82px;top:40px;width:97px;height:57px" role="img" aria-label="Foto: Viele Hände übereinander gelegt"></div>
      <div class="copy" style="top:106px">
        <p><b>Alles begann vor einigen Jahren,</b> als eine Gruppe von Menschen mit unterschiedlichsten Hintergründen und Erfahrungen sich zusammenschloss, um gemeinsam für die Rechte von Menschen mit Behinderungen einzutreten. Wir merkten schnell, dass es in unserer Gesellschaft noch immer viele Barrieren gibt, die das selbstbestimmte Leben von Menschen mit Behinderungen erschweren.</p>
        <p>Doch wir waren nicht bereit, uns damit abzufinden und beschlossen, aktiv zu werden. Wir begannen uns zu vernetzen, tauschten uns über unsere Erfahrungen aus und arbeiteten gemeinsam an Lösungen. So entstand die Idee, eine Organisation zu gründen, die sich für die Förderung von Kommunikation und Inklusion von Menschen mit Behinderungen einsetzt – und so wurde Merovalien geboren.</p>
        <p>In den Anfangsjahren war es oft schwierig, Unterstützung zu finden und unsere Ziele in die Tat umzusetzen. Doch wir ließen uns nicht entmutigen und arbeiteten hart daran, unsere Vision von einer inklusiven Gesellschaft zu verwirklichen. Heute sind wir stolz darauf, dass unser Verein bereits vielen Menschen mit Behinderungen helfen konnte und dass wir in der Gesellschaft immer mehr Gehör finden.</p>
        <p><b>Wir sind dankbar für jeden, der sich uns anschließt und uns dabei unterstützt, Barrieren abzubauen und Menschen mit Behinderungen eine Stimme zu geben.</b></p>
      </div>
    </div>
    <div class="block violet" style="top:1382px;height:462px">
      <h2 style="margin-top:18px">Warum haben<br>wir den Verein gegründet?</h2>
      <div class="pic group" style="left:64px;top:54px;width:132px;height:146px" role="img" aria-label="Foto: Gruppe junger Menschen, einer davon im Rollstuhl"></div>
      <div class="copy" style="top:208px">
        <p><b>Wir haben Merovalien gegründet,</b> weil uns die Bedürfnisse von Menschen mit Behinderungen am Herzen liegen und wir uns für ihre Rechte und eine inklusive Gesellschaft einsetzen wollen. Wir haben selbst erlebt, wie schwer es sein kann, Barrieren zu überwinden und sich Gehör zu verschaffen. Deshalb wollten wir eine Organisation schaffen, die sich für mehr Barrierefreiheit bei digitalen Medien, eine bessere zwischenmenschliche Kommunikation und die Förderung von Selbstbestimmung und Empowerment von Menschen mit Behinderungen einsetzt.</p>
        <p>Unser Ziel ist es, eine Gesellschaft zu schaffen, in der jeder Mensch unabhängig von einer Behinderung vollständig integriert ist und selbstbestimmt leben kann. Wir glauben, dass jeder Einzelne dazu beitragen kann und dass jede Stimme zählt. Wir möchten Menschen ermutigen, sich für die Rechte von Menschen mit Behinderungen einzusetzen und Barrieren abzubauen. Wir sind stolz darauf, Teil dieser Bewegung zu sein und hoffen, dass auch du dich uns anschließt!</p>
      </div>
    </div>
    <footer class="block footer" style="top:1844px;height:462px">
      <div class="foot-name" style="position:absolute;left:47px;top:38px">Merovalien</div>
      <div class="tagline" style="position:absolute;left:47px;top:65px;width:178px">
        <div class="rule">Verein für Teilhabe,</div>
        <div>Vielfalt und ein gleichberechtigtes</div>
        <div>Miteinander e.V.</div>
      </div>
      <ul class="list" style="position:absolute;left:47px;top:110px">
        <li>Merovalien e. V.</li>
        <li>c/o Lindenhofer Weg 14</li>
        <li>10437 Berlin</li>
        <li><span class="lbl">Tel.</span>: +49 (0) 3011 4820 500</li>
        <li><span class="lbl">Fax.</span>: +49 (0) 3011 4820 501</li>
        <li><span class="lbl">E-Mail</span>: info@merovalien.de</li>
        <li>Service</li>
        <li>Blog</li>
        <li>Privacy &amp; Policy</li>
        <li>Sitemap</li>
        <li>Barrierefreiheit</li>
      </ul>
      <div class="email" style="position:absolute;left:47px;top:322px">email</div>
      <ul class="list" style="position:absolute;left:47px;top:340px">
        <li class="newsletter">Abonnieren Sie unseren Newsletter!</li>
        <li>Impressum</li>
        <li>Datenschutzerklärung</li>
        <li>Cookie-Richtlinie</li>
      </ul>
      <div class="copyright" style="top:434px">© 2023, <b>MEROVALIEN</b> All rights reserved</div>
    </footer>
  </section>

  <section class="artboard desktop">
    <div class="block splash">
      <div class="name">merovalien</div>
      <div class="bar"></div>
    </div>
    <header class="block header" style="top:461px">
      <div class="brand"><span class="dot"></span>Merovalien</div>
      <nav class="nav"><a>Home</a><a class="active">Verein</a><a>Projekte</a><a>Team</a><a>Blog</a><a>Wir im Netz</a><a>Kontakt</a></nav>
      <div class="toggle"><svg width="9" height="9" viewBox="0 0 10 10"><circle cx="5" cy="5" r="2.2" fill="#fff"/><g stroke="#fff" stroke-width="1"><path d="M5 0v1.5M5 8.5V10M0 5h1.5M8.5 5H10"/></g></svg><svg width="9" height="9" viewBox="0 0 10 10"><path d="M7 1a4.2 4.2 0 1 0 2 6.5A3.5 3.5 0 0 1 7 1z" fill="#fff"/></svg></div>
    </header>
    <div class="block hero" style="top:521px">
      <div class="photo" role="img" aria-label="Foto: Vier Frauen, eine im Rollstuhl, halten bunte Sprechblasen vor einer weißen Wand"></div>
      <div class="cta">AUSFÜHRLICHE INFOS</div>
      <svg class="chev" width="16" height="9" viewBox="0 0 16 9"><path d="M1 1l7 7 7-7" fill="none" stroke="#fff" stroke-width="1.3"/></svg>
    </div>
    <div class="block navy" style="top:922px;height:460px">
      <header class="header" style="height:60px">
        <div class="brand"><span class="dot"></span>Merovalien</div>
        <nav class="nav"><a>Home</a><a class="active">Verein</a><a>Projekte</a><a>Team</a><a>Blog</a><a>Wir im Netz</a><a>Kontakt</a></nav>
        <div class="toggle"><svg width="9" height="9" viewBox="0 0 10 10"><circle cx="5" cy="5" r="2.2" fill="#fff"/><g stroke="#fff" stroke-width="1"><path d="M5 0v1.5M5 8.5V10M0 5h1.5M8.5 5H10"/></g></svg><svg width="9" height="9" viewBox="0 0 10 10"><path d="M7 1a4.2 4.2 0 1 0 2 6.5A3.5 3.5 0 0 1 7 1z" fill="#fff"/></svg></div>
      </header>
      <h2 style="margin-top:22px">Wie alles begann?</h2>
      <div class="pic hands" style="left:111px;top:128px;width:142px;height:292px" role="img" aria-label="Foto: Viele Hände übereinander gelegt"></div>
      <div class="copy" style="left:278px;top:124px;width:449px">
        <p><b>Alles begann vor einigen Jahren,</b> als eine Gruppe von Menschen mit unterschiedlichsten Hintergründen und Erfahrungen sich zusammenschloss, um gemeinsam für die Rechte von Menschen mit Behinderungen einzutreten. Wir merkten schnell, dass es in unserer Gesellschaft noch immer viele Barrieren gibt, die das selbstbestimmte Leben von Menschen mit Behinderungen erschweren.</p>
        <p>Doch wir waren nicht bereit, uns damit abzufinden und beschlossen, aktiv zu werden. Wir begannen uns zu vernetzen, tauschten uns über unsere Erfahrungen aus und arbeiteten gemeinsam an Lösungen. So entstand die Idee, eine Organisation zu gründen, die sich für die Förderung von Kommunikation und Inklusion von Menschen mit Behinderungen einsetzt – und so wurde Merovalien geboren.</p>
        <p>In den Anfangsjahren war es oft schwierig, Unterstützung zu finden und unsere Ziele in die Tat umzusetzen. Doch wir ließen uns nicht entmutigen und arbeiteten hart daran, unsere Vision von einer inklusiven Gesellschaft zu verwirklichen. Heute sind wir stolz darauf, dass unser Verein bereits vielen Menschen mit Behinderungen helfen konnte und dass wir in der Gesellschaft immer mehr Gehör finden.</p>
        <p><b>Wir sind dankbar für jeden, der sich uns anschließt und uns dabei unterstützt, Barrieren abzubauen und Menschen mit Behinderungen eine Stimme zu geben.</b></p>
      </div>
      <div class="up" style="left:727px;top:425px"><svg width="10" height="11" viewBox="0 0 10 11"><path d="M5 10V1M1 5l4-4 4 4" fill="none" stroke="#fff" stroke-width="1.3"/></svg></div>
    </div>
    <div class="block violet" style="top:1382px;height:462px">
      <header class="header" style="height:60px">
        <div class="brand"><span class="dot"></span>Merovalien</div>
        <nav class="nav"><a>Home</a><a class="active">Verein</a><a>Projekte</a><a>Team</a><a>Blog</a><a>Wir im Netz</a><a>Kontakt</a></nav>
        <div class="toggle"><svg width="9" height="9" viewBox="0 0 10 10"><circle cx="5" cy="5" r="2.2" fill="#fff"/><g stroke="#fff" stroke-width="1"><path d="M5 0v1.5M5 8.5V10M0 5h1.5M8.5 5H10"/></g></svg><svg width="9" height="9" viewBox="0 0 10 10"><path d="M7 1a4.2 4.2 0 1 0 2 6.5A3.5 3.5 0 0 1 7 1z" fill="#fff"/></svg></div>
      </header>
      <h2 style="margin-top:22px">Warum haben wir den Verein gegründet?</h2>
      <div class="copy" style="left:111px;top:141px;width:370px">
        <p><b>Wir haben Merovalien gegründet,</b> weil uns die Bedürfnisse von Menschen mit Behinderungen am Herzen liegen und wir uns für ihre Rechte und eine inklusive Gesellschaft einsetzen wollen. Wir haben selbst erlebt, wie schwer es sein kann, Barrieren zu überwinden und sich Gehör zu verschaffen. Deshalb wollten wir eine Organisation schaffen, die sich für mehr Barrierefreiheit bei digitalen Medien, eine bessere zwischenmenschliche Kommunikation und die Förderung von Selbstbestimmung und Empowerment von Menschen mit Behinderungen einsetzt.</p>
        <p>Unser Ziel ist es, eine Gesellschaft zu schaffen, in der jeder Mensch unabhängig von einer Behinderung vollständig integriert ist und selbstbestimmt leben kann. Wir glauben, dass jeder Einzelne dazu beitragen kann und dass jede Stimme zählt. Wir möchten Menschen ermutigen, sich für die Rechte von Menschen mit Behinderungen einzusetzen und Barrieren abzubauen. Wir sind stolz darauf, Teil dieser Bewegung zu sein und hoffen, dass auch du dich uns anschließt!</p>
      </div>
      <div class="pic group" style="left:505px;top:144px;width:222px;height:249px" role="img" aria-label="Foto: Gruppe junger Menschen, einer davon im Rollstuhl"></div>
    </div>
    <footer class="block footer" style="top:1844px;height:229px">
      <div class="foot-name" style="position:absolute;left:49px;top:42px">Merovalien</div>
      <ul class="list" style="position:absolute;left:49px;top:76px">
        <li>Merovalien e. V.</li>
        <li>c/o Lindenhofer Weg 14</li>
        <li>10437 Berlin</li>
        <li><span class="lbl">Tel.</span>: +49 (0) 3011 4820 500</li>
        <li><span class="lbl">Fax.</span>: +49 (0) 3011 4820 501</li>
        <li><span class="lbl">E-Mail</span>: info@merovalien.de</li>
      </ul>
      <ul class="list" style="position:absolute;left:357px;top:94px">
        <li>Service</li>
        <li>Blog</li>
        <li>Privacy &amp; Policy</li>
        <li>Sitemap</li>
        <li>Barrierefreiheit</li>
      </ul>
      <div class="tagline" style="position:absolute;left:585px;top:40px;width:186px">
        <div class="rule">Verein für Teilhabe,</div>
        <div>Vielfalt und ein gleichberechtigtes</div>
        <div>Miteinander e.V.</div>
      </div>
      <div class="email" style="position:absolute;left:585px;top:94px">email</div>
      <ul class="list" style="position:absolute;left:585px;top:112px">
        <li class="newsletter">Abonnieren Sie unseren Newsletter!</li>
        <li>Impressum</li>
        <li>Datenschutzerklärung</li>
        <li>Cookie-Richtlinie</li>
      </ul>
      <div class="up" style="left:727px;top:172px"><svg width="10" height="11" viewBox="0 0 10 11"><path d="M5 10V1M1 5l4-4 4 4" fill="none" stroke="#fff" stroke-width="1.3"/></svg></div>
      <div class="copyright" style="top:207px">© 2023, <b>MEROVALIEN</b> All rights reserved</div>
    </footer>
  </section>

</main>
</body>
</html>
```